Chiropractic office needs updated web site

take the information/content from my existing website and redesign it to be more efficient and modern looking. i have a logo already designed that i have provided the files for. my office sees primarily athletes and their families and is geared toward active, healthy people who have sports injuries.
Updates

i originally started the project in february 2019 but am now just able to post the project. i need a new deadline calculated from todays (6-9-19) date.

Target Market(s)

injured athletes looking for a specific type of chiropractor.

Industry/Entity Type

Health Care

Contact Information for Business Card

I have a logo already designed and will provide that to all designers!

Coding

Coded - Design and coding required

Number of Pages Required

1 page

Font styles to use
Sans Serif

Colors

Designer to choose colors to be used in the design.

Requirements
Must have
• the current information/content already contained in my current website, belvanspinefit.com. i want this info redesigned and/or transferred to a new template. i will also provide new updated photos for use on the new site!
Nice to have
• modern, minimalist, creative looking website
Should not have
• typical medical website with boring, over-used stock photos of doctors, nurses and generic family types

```html
<!DOCTYPE html>
<html lang="en">
<head>
<meta charset="utf-8">
<title>Belvan SpineFit – Chiropractic &amp; Sports Therapy</title>
<link rel="stylesheet" href="https://fonts.googleapis.com/css2?family=Montserrat:wght@400;600;700;800&family=Open+Sans:wght@400;600&display=swap">
<style>
:root{
  --teal:#1690b5;
  --teal-dark:#0d6f8f;
  --teal-light:#d7eef5;
  --red:#e0262b;
  --ink:#2b2f33;
  --muted:#6d7378;
  --line:#e3e6e8;
  --paper:#ffffff;
  --soft:#f5f7f8;
  --footer:#f1f3f4;
}
*{box-sizing:border-box;margin:0;padding:0}
html,body{width:1200px;height:4164px;overflow:hidden}
body{background:var(--paper);font-family:"Open Sans",Arial,sans-serif;color:var(--ink);font-size:14px;line-height:1.6}
h1,h2,h3,h4,.brand,.nav,.btn{font-family:"Montserrat",Arial,sans-serif}
.section-title{text-align:center;font-size:26px;font-weight:700;color:var(--ink)}
.section-title::after{content:"";display:block;width:44px;height:3px;background:var(--teal);margin:12px auto 0}
.btn{display:inline-block;background:var(--teal);color:#fff;font-size:13px;font-weight:600;padding:12px 26px;border-radius:3px;text-decoration:none}

/* header */
.site-header{height:112px;display:flex;align-items:center;padding:0 40px;background:#fff;position:relative;z-index:2}
.brand{display:flex;align-items:center;gap:10px;font-size:22px;font-weight:800;color:var(--teal);letter-spacing:1px}
.brand-dot{width:40px;height:40px;border-radius:50%;background:var(--teal)}
.nav{display:flex;gap:26px;margin-left:70px;font-size:12px;font-weight:600;color:var(--muted)}
.nav a{color:inherit;text-decoration:none}
.nav a.active{color:var(--teal);border-bottom:2px solid var(--teal);padding-bottom:4px}
.header-right{margin-left:auto;text-align:right}
.header-top{display:flex;gap:8px;justify-content:flex-end;align-items:center}
.social{width:14px;height:14px;border-radius:50%;background:var(--teal)}
.contact-btn{background:var(--red);color:#fff;font-size:12px;font-weight:600;padding:7px 16px;margin-left:8px;font-family:"Montserrat",sans-serif}
.call{margin-top:8px;font-size:11px;color:var(--muted)}
.call strong{display:flex;gap:6px;align-items:center;justify-content:flex-end;font-size:18px;color:var(--teal);font-family:"Montserrat",sans-serif}

/* hero */
.hero{height:708px;position:relative;background:linear-gradient(180deg,#c9d9c2 0%,#a9c08a 40%,#6f8f3f 75%,#4e6b2a 100%)}
.hero-text{position:absolute;left:150px;top:120px;color:#fff}
.hero-kicker{font-family:"Montserrat",sans-serif;font-size:26px;font-weight:600;letter-spacing:1px}
.hero h1{font-size:64px;line-height:1.1;font-weight:700;color:#fff;max-width:520px;text-shadow:0 2px 8px rgba(0,0,0,.2)}
.hero-sub{font-family:"Montserrat",sans-serif;font-size:22px;margin:14px 0 30px}

/* mission */
.mission{padding:70px 150px 0;height:340px}
.mission p{margin-top:22px;text-align:center;color:var(--muted);font-size:13px}
.mission p + p{margin-top:12px}

/* gallery */
.gallery{height:560px;position:relative}
.gallery .section-title{padding-top:20px}
.slide{position:absolute;border:6px solid #fff;box-shadow:0 4px 16px rgba(0,0,0,.18)}
.slide.main{left:220px;top:110px;width:760px;height:440px;background:linear-gradient(160deg,#9cc3d6,#c7b59a 55%,#7b6b55);z-index:2}
.slide.side-left{left:80px;top:140px;width:200px;height:380px;background:linear-gradient(160deg,#b9c7cf,#8b8f86)}
.slide.side-right{left:920px;top:140px;width:200px;height:380px;background:linear-gradient(160deg,#d1c5b2,#8e8171)}
.arrow{position:absolute;top:316px;font-size:26px;color:var(--ink);font-family:"Montserrat",sans-serif}
.dots{position:absolute;left:0;right:0;top:540px;display:flex;justify-content:center;gap:8px}
.dots span{width:8px;height:8px;border-radius:50%;background:#c5cbce}
.dots span.on{background:var(--teal)}

/* treatments */
.treatments{height:340px;padding-top:60px}
.treat-grid{display:grid;grid-template-columns:repeat(4,1fr);gap:30px;padding:40px 160px 0;text-align:center}
.treat-icon{width:60px;height:60px;margin:0 auto 12px;border-radius:50%;display:flex;align-items:center;justify-content:center}
.treat-icon.active{background:var(--teal)}
.treat h3{font-size:14px;font-weight:700;color:var(--ink)}
.treat p{font-size:11px;color:var(--muted);margin-top:6px;line-height:1.5}
.treat a{font-size:11px;color:var(--teal);font-weight:600;text-decoration:none}

/* doctors */
.doctor{position:relative;display:flex;align-items:flex-start;gap:60px;padding:0 140px}
.doctor h2{font-size:26px;font-weight:700}
.doctor h2::after{content:"";display:block;width:44px;height:3px;background:var(--teal);margin-top:10px}
.doctor-bio{flex:1}
.doctor-bio p{font-size:12px;color:var(--muted);margin-top:16px}
.drop{float:left;font-family:"Montserrat",sans-serif;font-size:40px;line-height:1;font-weight:700;color:var(--teal);margin:2px 8px 0 0}
.doctor .btn{margin-top:26px}
.portrait{width:280px;height:320px;flex:none}
.doctor-owen{height:440px;padding-top:60px}
.portrait.owen{background:linear-gradient(180deg,#e8ecef,#9fb5c7 60%,#3f5a78)}
.doctor-lena{height:452px;padding-top:60px}
.portrait.lena{background:linear-gradient(180deg,#f2e8e0,#c79878 55%,#6a4b3a)}

/* guide */
.guide{height:320px;background:linear-gradient(135deg,var(--teal-dark),var(--teal) 50%,#1fa7c9);text-align:center;color:#fff;padding-top:70px}
.guide h2{font-size:44px;font-weight:800;letter-spacing:1px}
.guide-sub{font-family:"Montserrat",sans-serif;font-size:13px;font-weight:600;letter-spacing:2px;margin-top:6px}
.guide-form{display:flex;justify-content:center;margin-top:36px}
.guide-input{width:320px;height:44px;background:#fff;color:#9aa0a4;font-size:12px;text-align:left;padding:12px 18px}
.guide-btn{height:44px;background:var(--red);color:#fff;font-family:"Montserrat",sans-serif;font-size:12px;font-weight:700;padding:14px 26px}

/* instagram */
.instagram{height:388px;padding-top:40px}
.insta-grid{display:grid;grid-template-columns:repeat(10,112px);grid-auto-rows:92px;gap:0;margin:36px 40px 0;width:1120px}
.insta-grid div:nth-child(4n+1){background:linear-gradient(135deg,#c9a88a,#7f6650)}
.insta-grid div:nth-child(4n+2){background:linear-gradient(135deg,#a9c3d1,#5f7d90)}
.insta-grid div:nth-child(4n+3){background:linear-gradient(135deg,#e0c6b4,#a47d66)}
.insta-grid div:nth-child(4n){background:linear-gradient(135deg,#b7c29c,#6c7d52)}

/* footer */
.site-footer{height:316px;background:var(--footer);padding:50px 140px 0;display:grid;grid-template-columns:1.4fr 1fr 1fr 1.3fr;gap:40px;position:relative}
.site-footer h4{font-size:14px;font-weight:700;margin-bottom:12px}
.site-footer p,.site-footer li{font-size:11px;color:var(--muted);list-style:none;line-height:1.9}
.site-footer .brand{font-size:18px;margin-bottom:14px}
.site-footer .brand-dot{width:30px;height:30px}
.copyright{position:absolute;left:0;right:0;bottom:0;height:44px;border-top:1px solid var(--line);text-align:center;font-size:11px;color:var(--muted);line-height:44px}
</style>
</head>
<body>

<header class="site-header">
  <div class="brand"><span class="brand-dot"></span>BELVAN SPINEFIT</div>
  <nav class="nav">
    <a class="active" href="#">Home</a><a href="#">Meet Location</a><a href="#">Treatments Offered</a><a href="#">New Patient Paperwork</a><a href="#">Scheduling</a><a href="#">Sociel</a><a href="#">Photo Gallery</a>
  </nav>
  <div class="header-right">
    <div class="header-top">
      <span class="social"></span><span class="social"></span><span class="social"></span><span class="social"></span>
      <span class="contact-btn">Contact Us</span>
    </div>
    <div class="call">Call Us For A Free Consultation
      <strong><svg width="16" height="16" viewBox="0 0 24 24"><path fill="#1690b5" d="M6.6 10.8a15 15 0 0 0 6.6 6.6l2.2-2.2c.3-.3.7-.4 1-.2 1.1.4 2.3.6 3.6.6.6 0 1 .4 1 1V20c0 .6-.4 1-1 1A17 17 0 0 1 3 4c0-.6.4-1 1-1h3.5c.6 0 1 .4 1 1 0 1.3.2 2.5.6 3.6.1.3 0 .7-.2 1z"/></svg>615.555.0142</strong>
    </div>
  </div>
</header>

<section class="hero" role="img" aria-label="Woman stretching her arms wide in a sunlit grassy field">
  <div class="hero-text">
    <div class="hero-kicker">CHIROPRACTIC:</div>
    <h1>For Relief, Healing, and Prevention</h1>
    <div class="hero-sub">Life Regain When Injury Ends</div>
    <a class="btn" href="#">Read More</a>
  </div>
</section>

<section class="mission">
  <h2 class="section-title">Mission Statement</h2>
  <p>Our goal at Belvan SpineFit is to help every athlete, weekend warrior and active family reach full recovery and peak physical performance through a partnership with our patients. By blending hands-on care with modern rehab methods, we create a lasting plan where the patient can manage their own health, train with confidence and return to the sport they love stronger than before.</p>
  <p>We combine chiropractic adjustment with soft tissue work, mobility training and sport specific coaching. Every patient receives a custom plan built around their goals, and our team stays with them from the first visit to the final game day.</p>
</section>

<section class="gallery">
  <h2 class="section-title">Photo Gallery</h2>
  <div class="slide side-left" role="img" aria-label="Athletes training outdoors"></div>
  <div class="slide main" role="img" aria-label="Group of women doing a fitness workout outdoors under a shade canopy"></div>
  <div class="slide side-right" role="img" aria-label="Athlete stretching during a session"></div>
  <span class="arrow" style="left:100px">&#8249;</span>
  <span class="arrow" style="left:1086px">&#8250;</span>
  <div class="dots"><span></span><span></span><span class="on"></span><span></span><span></span></div>
</section>

<section class="treatments">
  <h2 class="section-title">Treatments Offered</h2>
  <div class="treat-grid">
    <div class="treat">
      <div class="treat-icon"><svg width="40" height="40" viewBox="0 0 40 40"><rect x="15" y="4" width="10" height="20" rx="5" fill="none" stroke="#1690b5" stroke-width="2.5"/><path d="M10 18a10 10 0 0 0 20 0M20 28v8M14 36h12" fill="none" stroke="#1690b5" stroke-width="2.5"/></svg></div>
      <h3>Myofascial Release</h3>
      <p>Focused pressure eases tight fascia, restores motion and speeds recovery after hard training.</p>
      <a href="#">Read More</a>
    </div>
    <div class="treat">
      <div class="treat-icon"><svg width="40" height="40" viewBox="0 0 40 40"><rect x="8" y="6" width="24" height="30" rx="2" fill="none" stroke="#1690b5" stroke-width="2.5"/><path d="M14 16h12M14 22h12M14 28h8" stroke="#1690b5" stroke-width="2.5"/></svg></div>
      <h3>The Belvan Protocol</h3>
      <p>Our signature plan joins adjustment, rehab and strength work into one clear path back to play.</p>
      <a href="#">Read More</a>
    </div>
    <div class="treat">
      <div class="treat-icon active"><svg width="36" height="36" viewBox="0 0 40 40"><circle cx="20" cy="9" r="5" fill="#fff"/><path d="M20 15v12M12 20h16M20 27l-6 10M20 27l6 10" stroke="#fff" stroke-width="3" stroke-linecap="round"/></svg></div>
      <h3>Active Release Therapy</h3>
      <p>Movement based soft tissue care that breaks up scar tissue and frees muscles and nerves.</p>
      <a href="#">Read More</a>
    </div>
    <div class="treat">
      <div class="treat-icon"><svg width="40" height="40" viewBox="0 0 40 40"><circle cx="20" cy="20" r="7" fill="none" stroke="#1690b5" stroke-width="2.5"/><path d="M20 4v6M20 30v6M4 20h6M30 20h6M9 9l4 4M27 27l4 4M31 9l-4 4M13 27l-4 4" stroke="#1690b5" stroke-width="2.5"/></svg></div>
      <h3>Trigger Point Therapy</h3>
      <p>Targeted release of painful knots that refer pain and limit strength across the body.</p>
      <a href="#">Read More</a>
    </div>
  </div>
</section>

<section class="doctor doctor-owen">
  <div class="doctor-bio">
    <h2>Dr. Owen Belvan</h2>
    <p><span class="drop">DR</span>Dr. Owen Belvan is the owner and clinic director of Belvan SpineFit. He is a lifelong athlete who grew up playing every sport he could and went on to compete at the college level. After his own injuries kept him off the field, he found chiropractic care and knew it was his calling. He trained across the country with leading sports doctors and spent years caring for athletes from youth leagues to professional teams. Today he blends chiropractic adjustment, soft tissue therapy and strength coaching to help each patient heal faster and perform at their best.</p>
    <a class="btn" href="#">Read More</a>
  </div>
  <div class="portrait owen" role="img" aria-label="Portrait of Dr. Owen Belvan in a blue shirt"></div>
</section>

<section class="guide" role="region" aria-label="Free guide signup on a teal geometric pattern background">
  <h2>GET YOUR FREE GUIDE</h2>
  <div class="guide-sub">OWEN BELVAN IS THE OWNER AND CLINIC</div>
  <div class="guide-form">
    <div class="guide-input">Enter your email</div>
    <div class="guide-btn">GET FREEBIE NOW</div>
  </div>
</section>

<section class="doctor doctor-lena">
  <div class="portrait lena" role="img" aria-label="Portrait of Dr. Lena Hartwell smiling"></div>
  <div class="doctor-bio">
    <h2>Dr. Lena Hartwell</h2>
    <p><span class="drop">DR</span>Dr. Lena Hartwell graduated with honors from Northfield University, where she earned her Doctor of Chiropractic. She first became interested in health care as a massage therapist, working with runners and dancers who wanted more than short term relief. She saw how many patients needed a deeper answer to their pain and chose to study the spine, nerves and muscles that hold it all together. Her care is gentle, thorough and focused on lasting results.</p>
    <p>Since graduating, Dr. Hartwell has taught workshops on soft tissue therapy and joined the team to bring her skills to athletes of all ages. Her favorite part of the job is watching a patient return to the game feeling better than ever before.</p>
    <a class="btn" href="#">Read More</a>
  </div>
</section>

<section class="instagram">
  <h2 class="section-title">Flow Us On Instagram</h2>
  <div class="insta-grid" role="img" aria-label="Grid of Instagram photos of patients, athletes and clinic moments">
    <div></div><div></div><div></div><div></div><div></div><div></div><div></div><div></div><div></div><div></div>
    <div></div><div></div><div></div><div></div><div></div><div></div><div></div><div></div><div></div><div></div>
    <div></div><div></div><div></div><div></div><div></div><div></div><div></div><div></div><div></div><div></div>
  </div>
</section>

<footer class="site-footer">
  <div>
    <div class="brand"><span class="brand-dot"></span>BELVAN SPINEFIT</div>
    <p>We are proud to serve athletes and families with caring, hands-on treatment built to help every patient move, train and live better each day.</p>
  </div>
  <div>
    <h4>Quick Link</h4>
    <ul><li>Home</li><li>Meet Location</li><li>Treatments Offered</li><li>New Patient Paperwork</li><li>Scheduling</li><li>Sociel</li><li>Photo Gallery</li></ul>
  </div>
  <div>
    <h4>Support</h4>
    <ul><li>Home</li><li>About Us</li><li>Media Kit</li><li>Our Work</li><li>Blog</li><li>Contact</li><li>Contact Us</li></ul>
  </div>
  <div>
    <h4>Contact</h4>
    <p>Address : 200 Riverbend Rd<br>Franklin, TN 37000</p>
    <p>Tel : 615.555.0142<br>Fax : 615.555.0143</p>
    <p>Email : info@belvanspinefit.com</p>
  </div>
  <div class="copyright">© 2019 Belvan SpineFit. All Rights Reserved</div>
</footer>

</body>
</html>
```